River Stones, Evening Light Poster for American Indian Older Adults

We need am 11" x 17" poster designed for a health outreach project designed to reach older U.S. American Indians. The materials developed through this project will be distributed to American Indian and Alaska Native tribes, communities and tribal-serving organizations across the U.S. (more than 500 different tribes). If we find a successful design we will work with that designer to produce at least one other item we need design work for using the same look/feel and maybe other materials for this project. (more work!). The poster will include a set of facts (bulleted list on the attached document) that we would like presented in an "infographic" style. The design must be reflective of the American Indian culture and designed with older adults (65 and older) in mind. Imagery plays a strong role in the American Indian culture in the U.S. images of the heart, water, feathers, circle of life, etc. If you use photos of people they must include older adults and they must be American Indian (Native American). We prefer deep earth tones for the color scheme. The design must take into account design principles for older adults: 1. Try not to put colored font on colored background 2. Ensure high contrast for text 3. Font style should be sans serif, not cursive,decorative or heavily stylized because it is harder to read 4. Avoid using all caps 5. Don't print sideways or on top of images, shaded, backgrounds, etc. 6. All images should related specifically to the content of the text and be culturally appropriate for both older adults and American Indians. The final design should be easy to read and appeal to older American Indian adults. We need to incorporate three logos on the poster towards the bottom they should not be the center/focus of the poster. We also need to include a statement about who produced the materials- that can be very small below the logos at the bottom of the poster. We've attached the text for the poster and three logo files (note one is solid blue- we will finalize that after the document design is selected but need a placeholder for that logo.

Target Market(s)

Older adult (65 and older) American Indian and Alaska Natives and their family members in tribes, communities and tribal-serving organizations across the US

Font styles to use
Sans Serif

Requirements
Must have
• Must adhere to good design principles for older adults (listed in project description)
• Must feature culturally appropriate/targeted imagery and design look and feel

```html
<!DOCTYPE html>
<html lang="en">
<head>
<meta charset="UTF-8">
<title>River Stones, Evening Light</title>
<link href="https://fonts.googleapis.com/css2?family=Open+Sans:ital,wght@0,400;0,600;0,700;0,800;1,700;1,800&display=swap" rel="stylesheet">
<style>
  :root {
    --orange: #f26a1b;
    --orange-light: #f89a3c;
    --orange-pale: #fbd3b0;
    --navy: #1b3a6b;
    --ink: #2b2b2b;
    --white: #ffffff;
    --photo-a: #ece8e1;
    --photo-b: #d3cabd;
  }
  * { box-sizing: border-box; margin: 0; padding: 0; }
  html, body { width: 802px; height: 1200px; overflow: hidden; background: var(--white); }
  body { font-family: "Open Sans", Arial, sans-serif; color: var(--ink); }
  .poster { position: relative; width: 802px; height: 1200px; overflow: hidden; background: var(--white); }
  .waves { position: absolute; inset: 0; width: 802px; height: 1200px; }
  .photo {
    position: absolute; left: 30px; top: 40px; width: 400px; height: 580px;
    background: linear-gradient(180deg, var(--photo-a), var(--photo-b));
    border-radius: 20px;
  }
  .title {
    position: absolute; left: 440px; top: 190px; width: 345px;
    font-size: 44px; font-weight: 800; font-style: italic; line-height: 1.08;
    color: var(--navy); text-align: center;
  }
  .subtitle {
    position: absolute; left: 455px; top: 316px; width: 325px;
    font-size: 21px; font-weight: 600; line-height: 1.3;
    color: var(--orange); text-align: center;
  }
  .facts { position: absolute; left: 455px; top: 470px; width: 325px; list-style: none; }
  .fact { display: flex; align-items: center; gap: 16px; margin-bottom: 20px; min-height: 62px; }
  .fact-icon { flex: 0 0 56px; height: 56px; border-radius: 50%; }
  .fact-icon.orange { background: var(--orange); }
  .fact-icon.navy { background: var(--navy); }
  .fact-icon.pale { background: var(--orange-light); }
  .fact-text { font-size: 17px; line-height: 1.35; color: var(--ink); }
  .risk-note {
    position: absolute; left: 55px; top: 650px; width: 320px;
    font-size: 20px; font-weight: 700; font-style: italic; line-height: 1.3;
    color: var(--navy); text-align: center;
  }
  .risk-note em { color: var(--orange); font-style: italic; }
  .partners { position: absolute; left: 55px; top: 835px; width: 320px; text-align: center; }
  .partner { font-size: 32px; font-weight: 800; color: var(--navy); line-height: 1.2; margin-bottom: 18px; }
  .partner.small { font-size: 20px; }
  .badge {
    position: absolute; left: 535px; top: 845px; width: 215px; height: 215px;
    border-radius: 50%; border: 8px solid var(--navy); background: var(--white);
    display: flex; align-items: center; justify-content: center;
    box-shadow: 0 0 0 5px var(--white), 0 0 0 9px var(--navy);
  }
  .badge p { width: 150px; font-size: 23px; font-weight: 800; line-height: 1.2; color: var(--navy); text-align: center; }
  .contact-bar {
    position: absolute; left: 0; bottom: 0; width: 802px; height: 56px;
    background: var(--orange); display: flex; align-items: center; gap: 50px; padding-left: 60px;
    color: var(--white); font-size: 20px; font-weight: 600;
  }
  .contact-item { display: flex; align-items: center; gap: 10px; }
  .contact-item svg { width: 24px; height: 24px; fill: var(--white); }
</style>
</head>
<body>
<div class="poster">
  <svg class="waves" viewBox="0 0 802 1200" aria-hidden="true">
    <path d="M0 0 H802 V170 C720 110 640 150 560 110 C470 65 420 120 330 60 C250 15 120 55 0 25 Z" fill="var(--orange)"/>
    <path d="M420 0 H802 V120 C730 80 660 110 590 80 C520 50 480 60 420 0 Z" fill="var(--orange-light)"/>
    <path d="M500 1144 C600 1110 650 1070 802 1075 V1144 Z" fill="var(--orange-pale)"/>
    <path d="M0 1144 C200 1120 380 1135 520 1125 C640 1115 700 1095 802 1095 V1144 Z" fill="var(--orange-light)"/>
  </svg>

  <div class="photo" role="img" aria-label="Photo of an older couple dancing together"></div>

  <h1 class="title">River Stones, Evening Light</h1>
  <p class="subtitle">The River of Life Flows Through the Heart, Protecting the Mind and Body</p>

  <ul class="facts">
    <li class="fact"><span class="fact-icon orange" role="img" aria-label="Brain icon"></span><span class="fact-text">5.7 million Americans have Alzheimer's disease</span></li>
    <li class="fact"><span class="fact-icon orange" role="img" aria-label="Headstone icon"></span><span class="fact-text">Alzheimer's is the 6th leading cause of death</span></li>
    <li class="fact"><span class="fact-icon pale" role="img" aria-label="Elder icon"></span><span class="fact-text">1 out 10 people age 65 and older has Alzheimer's</span></li>
    <li class="fact"><span class="fact-icon navy" role="img" aria-label="Elder icon"></span><span class="fact-text">1 out of 3 American Indians over 65 develop dementia, including Alzheimer's</span></li>
  </ul>

  <p class="risk-note">Elders with <em>diabetes</em>, <em>heart disease</em>, or <em>high blood pressure</em> have a much higher risk of developing Alzheimer's or other dementias</p>

  <div class="partners">
    <p class="partner">Cendra</p>
    <p class="partner small">Circle of Elders Network</p>
    <p class="partner">Wellroot</p>
  </div>

  <div class="badge"><p>Make an appointment with your doctor!</p></div>

  <footer class="contact-bar">
    <span class="contact-item">
      <svg viewBox="0 0 24 24"><path d="M2 5h20v14H2z M2 5l10 8 10-8" fill="none" stroke="#fff" stroke-width="2"/></svg>
      info@cendra.org
    </span>
    <span class="contact-item">
      <svg viewBox="0 0 24 24"><path d="M6.6 10.8a15 15 0 006.6 6.6l2.2-2.2a1 1 0 011-.25 11.4 11.4 0 003.6.6 1 1 0 011 1V20a1 1 0 01-1 1A17 17 0 013 4a1 1 0 011-1h3.5a1 1 0 011 1 11.4 11.4 0 00.6 3.6 1 1 0 01-.25 1z"/></svg>
      888-555-0147
    </span>
  </footer>
</div>
</body>
</html>
```